captivating, innovative, real estate flyer, double sided

new boutique agency with highly experienced agents,
we have a logo for perch estates logo font in cocogoose. our text font is avenier black, colours are teal 326c charcoal is 426u.
we are all lower case lettering also except for ESTATES all correspondence is lower case also.

what we are looking for:

promoting our services - buy sell rent holiday - market appriasals/whats your property worth, we are located in the stunning jervis bay on south coast of australia postcodes 2540 and 2541.

we will upload the logo for you. either the white or the dark logo we don't mind. (can provide a high res for the dark logo when required)
we would like something a bit different and not comical but entertaining with what we do. we want to be taken seriously but something that clients will remember and possibly something that will stick in their heads. more inclined for a graphical rather than word play

as a promotion.
we would like to offer any clients that list their property for sale with us.
Up to the value of $350.00 either a carpenter pre listing (this is free of charge if they list with us)
an interior designer pre listing for staging of the home
a cleaner pre listing or for a settlement clean

if this could be incorporated on one side only as we are looking for 2 sided brochures.(the promo on one side only)

details that need to be on the brochures are
leonie marsh 0417 862 094 leonie@perchestates.example.com.au
marion pendle 0419/ 537 281 marion@perchestats.example.com.au
office 02 491 72 308 / 1300 48 73 91 info@perchestates.example.com.au

Target Market(s)

all sellers

Industry/Entity Type

Real Estate

Font styles to use
Other font styles liked:
• cocogoose for logo and avenier for text

Colors
00a990
1b1b1b
474747
33b8a4

Requirements
Must have
• light and catchy
Nice to have
• funny but catchy, smart and sophisticated, unusual not the normal for a real estate agency
• teal and charcoal or white it is not a problem if we have either of the logos
Should not have
• pictures of people, comics, the word VALUE is a must not have,

```html
<!DOCTYPE html>
<html lang="en">
<head>
<meta charset="utf-8">
<title>perch estates – find your dream home flyer</title>
<link href="https://fonts.googleapis.com/css2?family=Nunito+Sans:wght@400;700;900&family=Roboto+Condensed:wght@300;400;700;800&family=Open+Sans:wght@400;600&display=swap" rel="stylesheet">
<style>
  :root {
    --teal: #1fa99e;
    --teal-light: #33b8a4;
    --charcoal: #474747;
    --ink: #1b1b1b;
    --panel-grey: #a3a3a3;
    --stage: #e6e6e6;
    --white: #ffffff;
  }
  * { box-sizing: border-box; margin: 0; padding: 0; }
  html, body { width: 1200px; height: 1200px; overflow: hidden; }
  body { background: var(--stage); font-family: "Open Sans", sans-serif; }

  .flyer {
    position: absolute; left: 200px; top: 34px;
    width: 800px; height: 1132px;
    background: var(--white); overflow: hidden;
    box-shadow: 0 10px 30px rgba(0,0,0,.18);
  }

  .hero-photo {
    position: absolute; left: 0; top: 0; width: 800px; height: 430px;
    background: linear-gradient(180deg, #8e97a8 0%, #c8b8c0 22%, #8fc4d2 42%, #6a8f9c 62%, #c9cdd1 82%, #a9aaa8 100%);
  }
  .hero-rule { position: absolute; left: 0; top: 422px; width: 520px; height: 8px; background: var(--teal); }

  .logo {
    position: absolute; right: 40px; top: 40px;
    font-family: "Nunito Sans", sans-serif; font-weight: 900;
    font-size: 42px; line-height: 1; color: var(--teal); letter-spacing: -0.5px;
  }

  .info-panel {
    position: absolute; left: 520px; top: 380px; width: 280px; height: 680px;
    background: var(--panel-grey);
  }

  .house-photo {
    position: absolute; border-radius: 50%;
    border: 8px solid var(--teal); box-shadow: inset 0 0 0 5px var(--white);
  }
  .house-photo--large { left: 600px; top: 290px; width: 180px; height: 180px;
    background: linear-gradient(180deg, #8fb6e0 0%, #c5d8ea 35%, #9a5545 55%, #7a4a3e 72%, #5f8c3a 100%); }
  .house-photo--small { left: 500px; top: 380px; width: 130px; height: 130px;
    background: linear-gradient(180deg, #7fa6d8 0%, #b43a2a 38%, #b59a72 60%, #8a7a5c 80%, #5b7a3a 100%); }

  .headline {
    position: absolute; left: 40px; top: 462px;
    font-family: "Roboto Condensed", sans-serif; font-weight: 800;
    font-size: 60px; line-height: 0.95; text-transform: uppercase;
  }
  .headline__lead { color: var(--charcoal); display: block; }
  .headline__accent { color: var(--teal); display: block; }

  .section-pill {
    position: absolute; left: 40px; top: 612px; width: 360px; height: 38px;
    background: var(--charcoal); color: var(--white); border-radius: 0 19px 19px 0;
    font-family: "Roboto Condensed", sans-serif; font-weight: 700; font-size: 21px;
    line-height: 38px; padding-left: 18px;
  }

  .intro {
    position: absolute; left: 40px; top: 668px; width: 440px;
    font-size: 12px; line-height: 1.4; color: var(--ink); text-align: justify;
  }

  .promo { position: absolute; left: 40px; top: 750px; font-family: "Roboto Condensed", sans-serif; text-transform: uppercase; }
  .promo__price { font-weight: 700; font-size: 124px; line-height: 1; color: var(--teal); letter-spacing: -1px; }
  .promo__line { font-weight: 800; font-size: 44px; line-height: 1; color: var(--charcoal); }
  .promo__line--large { font-size: 58px; font-weight: 400; letter-spacing: 1px; }

  .services { position: absolute; left: 548px; top: 520px; width: 230px; color: var(--white); }
  .services__kicker { font-family: "Roboto Condensed", sans-serif; font-weight: 700; font-size: 26px; line-height: 1; }
  .services__title { font-family: "Roboto Condensed", sans-serif; font-weight: 300; font-size: 36px; line-height: 1.1; padding-left: 8px; }
  .services__list { list-style: none; margin-top: 18px; }
  .services__list li {
    position: relative; padding-left: 14px; margin-bottom: 6px;
    font-size: 11px; line-height: 1.35; color: var(--ink);
  }
  .services__list li::before {
    content: ""; position: absolute; left: 0; top: 5px; width: 6px; height: 6px;
    border-radius: 50%; background: var(--teal);
  }

  .agent { position: absolute; left: 548px; width: 240px; }
  .agent--first { top: 730px; }
  .agent--second { top: 810px; }
  .agent__name { font-family: "Roboto Condensed", sans-serif; font-weight: 700; font-size: 22px; line-height: 1.1; color: var(--white); margin-bottom: 8px; }
  .agent__detail { display: flex; align-items: center; gap: 6px; font-size: 11px; color: var(--ink); margin-bottom: 4px; padding-left: 6px; }
  .agent__detail svg { width: 11px; height: 11px; flex: none; }

  .location-map {
    position: absolute; left: 572px; top: 900px; width: 210px; height: 150px;
    background: linear-gradient(135deg, #eef0ea 0%, #dfe6d8 55%, #cfdcea 100%);
    border: 4px solid var(--white); box-shadow: 0 2px 6px rgba(0,0,0,.2);
  }

  .contact-band {
    position: absolute; left: 0; top: 1060px; width: 800px; height: 72px;
    background: var(--teal); color: var(--white);
    display: flex; align-items: center; gap: 60px; padding-left: 40px;
    font-family: "Nunito Sans", sans-serif; font-weight: 700; font-size: 19px;
  }
  .contact-band__item { display: flex; align-items: center; gap: 8px; }
  .contact-band__item svg { width: 16px; height: 16px; }
</style>
</head>
<body>
  <main class="flyer">
    <div class="hero-photo" role="img" aria-label="Photograph of a rocky beach at sunset with calm water and distant headland"></div>
    <div class="hero-rule"></div>
    <div class="logo">perch ESTATES</div>

    <div class="info-panel"></div>
    <div class="house-photo house-photo--large" role="img" aria-label="Photograph of a red brick two storey house with green lawn"></div>
    <div class="house-photo house-photo--small" role="img" aria-label="Photograph of a stone house with a red tiled roof"></div>

    <h1 class="headline">
      <span class="headline__lead">Find your</span>
      <span class="headline__accent">Dream home</span>
    </h1>

    <div class="section-pill">Why choose perch estates?</div>
    <p class="intro">perch estates is one of the south coast's newest independent boutique real estate agencies. our many years of local experience, unparalleled standard of excellence and genuine passion for property ensure we guarantee you a personalised property service which caters to all your real estate needs.</p>

    <div class="promo">
      <div class="promo__price">$350.00</div>
      <div class="promo__line">Either a carpenter</div>
      <div class="promo__line promo__line--large">Pre listing</div>
    </div>

    <section class="services">
      <div class="services__kicker">promoting</div>
      <div class="services__title">our services</div>
      <ul class="services__list">
        <li>buy sell rent holiday</li>
        <li>market appriasals/whats your property worth</li>
        <li>we are located in the stunning jervis bay on south coast of australia postcodes 2540 and 2541</li>
      </ul>
    </section>

    <div class="agent agent--first">
      <div class="agent__name">leonie marsh</div>
      <div class="agent__detail"><svg viewBox="0 0 16 16"><path d="M4 1l3 3-2 2c1 2 3 4 5 5l2-2 3 3-2 2C7 14 2 9 2 3z" fill="#1b1b1b"/></svg>0417 862 094</div>
      <div class="agent__detail"><svg viewBox="0 0 16 16"><rect x="1" y="3" width="14" height="10" rx="1" fill="#1b1b1b"/><path d="M1 4l7 5 7-5" stroke="#a3a3a3" fill="none"/></svg>leonie@perchestates.example.com.au</div>
    </div>
    <div class="agent agent--second">
      <div class="agent__name">marion pendle</div>
      <div class="agent__detail"><svg viewBox="0 0 16 16"><path d="M4 1l3 3-2 2c1 2 3 4 5 5l2-2 3 3-2 2C7 14 2 9 2 3z" fill="#1b1b1b"/></svg>0419/ 537 281</div>
      <div class="agent__detail"><svg viewBox="0 0 16 16"><rect x="1" y="3" width="14" height="10" rx="1" fill="#1b1b1b"/><path d="M1 4l7 5 7-5" stroke="#a3a3a3" fill="none"/></svg>marion@perchestats.example.com.au</div>
    </div>

    <div class="location-map" role="img" aria-label="Street map of the jervis bay office location"></div>

    <footer class="contact-band">
      <span class="contact-band__item"><svg viewBox="0 0 16 16"><path d="M4 1l3 3-2 2c1 2 3 4 5 5l2-2 3 3-2 2C7 14 2 9 2 3z" fill="#ffffff"/></svg>1300 48 73 91</span>
      <span class="contact-band__item"><svg viewBox="0 0 16 16"><rect x="1" y="3" width="14" height="10" rx="1" fill="#ffffff"/><path d="M1 4l7 5 7-5" stroke="#1fa99e" fill="none"/></svg>info@perchestates.example.com.au</span>
    </footer>
  </main>
</body>
</html>
```